Webdesign

We are value investment firm in Denver, Colorado. We are a small but a very unique firm. We are looking for a minimalistic and clean design. We are competing against competitors that usually larger than we are, but we need to have a design that is better than theirs. Our clients put a tremendous trust in us when they let us manage their life savings. This website has to communicate trust but without traditional cliches (dollar bills, glasses, Harbor Ledger Gazette).
We had a coder/designer create our current website a few weeks ago http://brindlecrest.com/qovapx , we are not thrilled about the design. We are attaching our company's presentation, we'd like the design to be closer to the colors of that presentation.
We are looking for both design and coding (wordpress).
Updates
we will pay additional $200 for wordpress implementation
A few points of clarifications about design:
- don't use pictures of strangers
- we are a Denver/Colorado firm, if you use pictures use Denver/Colorado pictures
- full width website is probably what we are looking
- maybe parallax type of design
This theme http://lomirstudio.com/WP/Tesseron/ is how we see the new design
Industry/Entity Type
Investment

```html
<!DOCTYPE html>
<html lang="en">
<head>
<meta charset="utf-8">
<title>Ravelstone — Private Portfolio Management</title>
<link rel="stylesheet" href="https://fonts.googleapis.com/css2?family=Open+Sans:wght@400;600&family=Roboto+Condensed:wght@300;400;700&family=Tinos:wght@400&display=swap">
<style>
  :root {
    --navy: #0f3470;
    --ink: #1c3766;
    --nav-text: #444444;
    --white: #ffffff;
    --page: #ffffff;
    --search-hint: #9a9a9a;
    --search-icon: #a8a8a8;
    --card-blue: #1b72c8;
    --card-cyan: #29c5fc;
    --card-red: #f53c3c;
    --footer-text: #333333;
  }
  * { margin: 0; padding: 0; box-sizing: border-box; }
  html, body { width: 1200px; height: 875px; overflow: hidden; background: var(--page); }
  body { position: relative; font-family: "Open Sans", Arial, sans-serif; }

  .site-header { position: absolute; top: 0; left: 0; width: 1200px; height: 67px; background: var(--white); box-shadow: 0 1px 3px rgba(0,0,0,.15); z-index: 2; }
  .brand { position: absolute; left: 73px; top: 16px; font-family: "Tinos", Georgia, serif; font-size: 30px; color: var(--navy); letter-spacing: .5px; line-height: 34px; }
  .main-nav { position: absolute; top: 0; left: 472px; height: 67px; display: flex; font-family: "Open Sans", Arial, sans-serif; font-size: 12.5px; }
  .main-nav a { display: block; height: 67px; line-height: 67px; color: var(--nav-text); text-decoration: none; text-transform: uppercase; }
  .main-nav .home { width: 103px; text-align: center; background: var(--navy); color: var(--white); }
  .main-nav .about { margin-left: 12px; }
  .main-nav .invest { margin-left: 45px; }
  .main-nav .content { margin-left: 50px; }
  .main-nav .career { margin-left: 45px; }
  .main-nav .contact { margin-left: 45px; }

  .hero { position: absolute; top: 67px; left: 0; width: 1200px; height: 592px; }
  .hero-photo { position: absolute; inset: 0; background: linear-gradient(180deg, #c9cdcf 0%, #dcdedd 22%, #b8b3a0 40%, #8a8568 52%, #5b5a3c 64%, #3b4026 80%, #2d3519 100%); }
  .tagline { position: absolute; top: 67px; left: 28px; width: 1172px; text-align: center; font-family: "Roboto Condensed", "Arial Narrow", sans-serif; font-weight: 300; font-size: 24.5px; line-height: 29.5px; color: var(--ink); }
  .search { position: absolute; top: 212px; left: 235px; width: 736px; height: 62px; background: var(--white); border-radius: 8px; }
  .search span { position: absolute; left: 22px; top: 0; line-height: 62px; font-size: 20px; color: var(--search-hint); }
  .search svg { position: absolute; right: 15px; top: 12px; }
  .mission { position: absolute; top: 356px; left: 87px; width: 1032px; height: 108px; border: 1px solid rgba(255,255,255,.85); background: rgba(0,0,0,.12); display: flex; align-items: center; justify-content: center; text-align: center; font-family: "Roboto Condensed", "Arial Narrow", sans-serif; font-weight: 700; font-size: 31.5px; line-height: 36px; color: var(--white); }

  .social { position: absolute; top: 680px; left: 74px; display: flex; gap: 2px; }
  .social-card { position: relative; width: 351px; height: 128px; color: var(--white); }
  .social-card.friendloop { background: var(--card-blue); width: 352px; }
  .social-card.chirpline { background: var(--card-cyan); }
  .social-card.orbitnet { background: var(--card-red); }
  .social-card .badge { position: absolute; left: 12px; top: 12px; width: 66px; height: 66px; border-radius: 50%; background: var(--white); }
  .social-card p { position: absolute; left: 99px; top: 17px; width: 235px; font-size: 12px; line-height: 16.5px; }
  .social-card h2 { position: absolute; left: 15px; top: 93px; font-size: 17px; font-weight: 400; }

  .copyright { position: absolute; top: 828px; left: 0; width: 1200px; text-align: center; font-size: 11.5px; color: var(--footer-text); }
</style>
</head>
<body>
  <header class="site-header">
    <div class="brand">Ravelstone</div>
    <nav class="main-nav">
      <a class="home" href="#">Home</a>
      <a class="about" href="#">About Us</a>
      <a class="invest" href="#">Invest Differently</a>
      <a class="content" href="#">Content</a>
      <a class="career" href="#">Career</a>
      <a class="contact" href="#">Contact Us</a>
    </nav>
  </header>

  <section class="hero">
    <div class="hero-photo" role="img" aria-label="Colorado mountain landscape under a hazy sky, forested hills and a dirt trail in the foreground"></div>
    <p class="tagline">A disciplined, process-driven, value investment firm that provides a private portfolio management service<br>tailored to individual and institutional client stiredofin-the-box, cookie-cutter,<br>buy-and-hope investment products.</p>
    <div class="search">
      <span>Search</span>
      <svg width="38" height="38" viewBox="0 0 38 38" aria-hidden="true">
        <circle cx="15" cy="15" r="11.5" fill="none" stroke="var(--search-icon)" stroke-width="4.5"/>
        <line x1="23.5" y1="23.5" x2="34" y2="34" stroke="var(--search-icon)" stroke-width="6" stroke-linecap="round"/>
      </svg>
    </div>
    <div class="mission">Our goal is to help the rich, and the aspiring rich, become richer while<br>sleeping well at night.</div>
  </section>

  <section class="social">
    <article class="social-card friendloop">
      <span class="badge"></span>
      <p>Lorem Ipsum is simply dummy text of the printing and typesetting industry Lorem Ipsum has been the.</p>
      <h2>Connect with Friendloop</h2>
    </article>
    <article class="social-card chirpline">
      <span class="badge"></span>
      <p>Lorem Ipsum is simply dummy text of the printing and typesetting industry Lorem Ipsum has been the.</p>
      <h2>Connect with Chirpline</h2>
    </article>
    <article class="social-card orbitnet">
      <span class="badge"></span>
      <p>Lorem Ipsum is simply dummy text of the printing and typesetting industry Lorem Ipsum has been the.</p>
      <h2>Connect with Orbitnet</h2>
    </article>
  </section>

  <footer class="copyright">Copyright © 2014 Ravelstone. All Rights Reserved</footer>
</body>
</html>
```